Flyer-Design - Coaching & Supervision für freib. Dipl.-Psychologin - BITTE KEINE WEITEREN DESINGS
Zielgruppe
--------- An alle, die überlegen mitzumachen - ich habe gerade als ungefähren Zeitplan, dass ich mich bis Donnerstag Abend (27.01.) entscheide, damit dann am Freitag (+evtl. Wochenende) noch Zeit für das Feintuning ist. -------------------
Ich bin Diplom-Psychologin und arbeite unter anderem freiberuflich als Coach und Supervisorin. Für diese Arbeit brauche ich einen Flyer. Ich habe bereits ein Konzept mit den Inhalten erstellt und brauche dafür nun ein professionelles Layout.
Aufgabenstellung
Anbei finden Sie das Konzept 1x als ppt (inklusive ausprobierter Alternativen zu den Fotos) und 1x als pdf.
Der Flyer hat als zentrales Thema „sich verändern / sich auf den Weg machen“ sowie die Analogie, dass ein gutes Coachinggespräch wie eine Bergtour ist.
Ich habe viel Vorarbeit gemacht (Inhalte stehen, Fotos sind recherchiert…) – sehr gerne können Sie sich kreativ ausleben und was völlig Neues / alles anders machen, es wäre aber auch ok, wenn das bereits Erarbeitete einfach graphisch aufgepimpt und professionalisiert wird.
Mein Wunsch: Ich weiß, dass der Flyer sehr voll ist. Aber ich möchte bewusst relativ viel Info dort unterbringen. Deshalb wäre es gut, wenn die Grafik des Flyers eine gewisse Leichtigkeit beinhaltet, die den vielen Text eher kaschiert. Also nicht zu verschnörkelt, sondern eher schlicht, hell und das Auge entlastend. Ich wünsche mir warme Farbtöne, die einladen und nicht zu kühl-modern wirken.
Logo:
Das Logo habe ich hier auf der Seite gestaltmarkt.de entwickeln lassen und habe alle Rechte daran. Es kann bei Bedarf auch angepasst werden.
Aktuell ist das Logo in grün, da ich dadurch den Naturbezug meiner Metapher mit aufgreife und weil die gerade entstehende Homepage, aktuell auch grün als Grundfarbe hat. Allerdings werde ich die Homepage auch noch professional überarbeiten lassen. Anbei einen Screenshot wie die Startseite der Homepage im Moment so ca. aussieht.
Bilder:
Die Fotos von mir hat ein Fotograf gemacht und ich darf sie verwenden.
Die Landschaftsbilder habe ich kostenlos und lizenzfrei von Lumora Bild ( https://bild.lumora-fotos.de/de/frei ) und von Fotelix ( https://fotelix-bilder.de/de/ ) heruntergeladen.
Falls Sie andere Bilder besser fänden und diese vorschlagen wollen, dann finden Sie weitere Details zu meinen Wünschen an die Bilder im Dokument „SelmK_AusschreibungDetails“
Die Landkarte ist ein Screenshot von KartoWeltNetz. Dort steht i..

```html
<!DOCTYPE html>
<html lang="de">
<head>
<meta charset="utf-8">
<title>Coaching &amp; Supervision – Flyer Innenseite</title>
<link href="https://fonts.googleapis.com/css2?family=Delius&family=Gafata&display=swap" rel="stylesheet">
<style>
  :root {
    --paper: #f3f3f0;
    --green: #2a7f2a;
    --green-box: #1f7a26;
    --ink: #2b2b2b;
    --rule: #d9d9d4;
    --sky-top: #bfe0ee;
    --sky-bottom: #fbfcfa;
  }
  * { margin: 0; padding: 0; box-sizing: border-box; }
  html, body { width: 1200px; height: 848px; overflow: hidden; background: var(--paper); }
  body { font-family: "Gafata", "Segoe UI", sans-serif; color: var(--ink); }
  .spread { position: relative; width: 1200px; height: 848px; }
  .panel { position: absolute; top: 0; width: 400px; height: 848px; }
  .panel--left { left: 0; background: linear-gradient(180deg, var(--sky-top) 0%, var(--sky-bottom) 28%, #ffffff 40%); }
  .panel--middle { left: 400px; border-left: 1px solid var(--rule); }
  .panel--right { left: 800px; border-left: 1px solid var(--rule); }
  .abs { position: absolute; }
  .headline { font-family: "Delius", cursive; color: var(--green); font-size: 24px; line-height: 27px; font-weight: 400; }
  .headline--center { text-align: center; }
  .copy { font-size: 13.6px; line-height: 17px; }
  .copy--justify { text-align: justify; hyphens: manual; }
  .copy p + p { margin-top: 4px; }

  /* left panel */
  .checklist { list-style: none; left: 32px; top: 178px; width: 360px; }
  .checklist li { position: relative; padding-left: 37px; font-size: 13.6px; line-height: 17px; margin-bottom: 12px; }
  .checklist svg { position: absolute; left: 0; top: -3px; }
  .hero-photo { left: 0; top: 364px; width: 400px; height: 484px;
    background: linear-gradient(180deg, #f6ecd2 0%, #d8b27a 35%, #8a6a42 65%, #4a3a26 100%); }
  .quote-box { left: 29px; top: 628px; width: 345px; height: 160px; background: var(--green-box); color: #fff; text-align: center; padding-top: 22px; }
  .quote-box__title { font-family: "Delius", cursive; font-size: 25px; line-height: 30px; margin-bottom: 10px; }
  .quote-box__text { font-size: 13.6px; line-height: 17.5px; font-style: italic; padding: 0 24px; }
  .quote-mark { font-family: "Delius", cursive; color: #fff; font-size: 56px; line-height: 1; font-weight: 700; }

  /* middle panel */
  .topic-grid { left: 22px; top: 534px; width: 356px; height: 266px; }
  .topic-grid__v { position: absolute; left: 176px; top: 0; width: 2px; height: 266px; background: var(--green); }
  .topic-grid__h { position: absolute; left: 0; top: 132px; width: 356px; height: 2px; background: var(--green); }
  .topic { position: absolute; width: 170px; }
  .topic__title { font-size: 14px; line-height: 18px; margin-bottom: 3px; }
  .topic__text { font-size: 12px; line-height: 15.5px; }

  /* right panel */
  .values { list-style: none; left: 28px; top: 412px; }
  .values li { font-size: 13.6px; line-height: 21px; padding-left: 20px; position: relative; }
  .values li::before { content: "•"; position: absolute; left: 2px; }
  .step-label { font-size: 13.2px; line-height: 17px; text-align: center; width: 100px; }
</style>
</head>
<body>
<div class="spread">

  <!-- Left panel -->
  <section class="panel panel--left">
    <h2 class="headline abs" style="left:40px; top:68px; width:350px;">Ein gutes Coachinggespräch ist wie eine gemeinsame Bergtour…</h2>
    <ul class="checklist abs">
      <li><svg width="24" height="24" viewBox="0 0 24 24" fill="none" stroke="#2a7f2a" stroke-width="1.8" stroke-linecap="round"><path d="M20 9.5A9 9 0 1 1 15.5 4"/><path d="M7 11.5l4 4 10-11"/></svg>Sie bestimmen das Thema – „Ihren Berg“.</li>
      <li><svg width="24" height="24" viewBox="0 0 24 24" fill="none" stroke="#2a7f2a" stroke-width="1.8" stroke-linecap="round"><path d="M20 9.5A9 9 0 1 1 15.5 4"/><path d="M7 11.5l4 4 10-11"/></svg>Sie bestimmen das Tempo.</li>
      <li><svg width="24" height="24" viewBox="0 0 24 24" fill="none" stroke="#2a7f2a" stroke-width="1.8" stroke-linecap="round"><path d="M20 9.5A9 9 0 1 1 15.5 4"/><path d="M7 11.5l4 4 10-11"/></svg>Sie entdecken Ihre eigenen Ressourcen während Sie sich Schritt für Schritt Ihrem Ziel nähern.</li>
    </ul>
    <p class="copy abs" style="left:33px; top:294px; width:340px;">Gemeinsam erkunden wir, welche Wege es zu Ihrem Ziel gibt. Ich begleite Sie auf allen Etappen. Ich helfe Ihnen, sich unterwegs zu orientieren.</p>
    <div class="hero-photo abs" role="img" aria-label="Foto: Wanderer steigt im Gegenlicht der Abendsonne einen Hang hinauf, dahinter eine Schluchtenlandschaft"></div>
    <div class="quote-box abs">
      <div class="quote-box__title">Wir gehen den Weg:</div>
      <p class="quote-box__text">mit Offenheit, mit Neugierde, mit einem Lachen, mit einem klaren Blick, mit Pausen, mit Ausdauer, mit Freude, mit Motivation, mit allen Sinnen und allen Emotionen</p>
    </div>
    <span class="quote-mark abs" style="left:54px; top:606px;">“</span>
    <span class="quote-mark abs" style="left:322px; top:758px;">”</span>
  </section>

  <!-- Middle panel -->
  <section class="panel panel--middle">
    <h2 class="headline headline--center abs" style="left:0; top:68px; width:400px;">Was ist Coaching &amp;<br>Supervision?</h2>
    <div class="copy copy--justify abs" style="left:26px; top:140px; width:348px;">
      <p>Im Coaching und in der Supervision haben Sie die Mög­lichkeit, Ihr eigenes Handeln im beruflichen Kontext zu reflektieren.</p>
      <p>Mit Hilfe von strukturierten Gesprächen und aus­gewählten Methoden begleite ich Sie dabei, in einem geschützten Rahmen eigene Lösungen zu entwickeln und umzusetzen.</p>
    </div>
    <h2 class="headline headline--center abs" style="left:0; top:308px; width:400px;">Geht es nur um<br>berufliche Themen? Jein.</h2>
    <p class="copy copy--justify abs" style="left:26px; top:374px; width:348px;">Private Themen können Kraftgeber und Krafträuber sein und sich auf berufliche Themen auswirken. Es geht oft um die Balance im Leben und deshalb ist es gut beides im Auge zu haben. Coaching ist aber keine Therapie.</p>
    <h2 class="headline headline--center abs" style="left:0; top:486px; width:400px;">Häufige Themenfelder:</h2>
    <div class="topic-grid abs">
      <div class="topic-grid__v"></div>
      <div class="topic-grid__h"></div>
      <div class="topic" style="left:0; top:30px;">
        <div class="topic__title">Berufliche Kompetenzen</div>
        <div class="topic__text">Führung, Umgang mit Veränderungen, herausfor­dernde Aufgaben meistern,…</div>
      </div>
      <div class="topic" style="left:190px; top:30px;">
        <div class="topic__title">Persönlichen Kompetenzen</div>
        <div class="topic__text">neue Perspektiven, Work-Live-Balance, Konfliktverhalten, …</div>
      </div>
      <div class="topic" style="left:0; top:182px;">
        <div class="topic__title">Team</div>
        <div class="topic__text">Zusammenarbeit, Kommu­nikation, Konflikte…</div>
      </div>
      <div class="topic" style="left:190px; top:182px;">
        <div class="topic__title">Supervisorische Fallarbeit</div>
        <div class="topic__text">schwierige Fälle / Klienten</div>
      </div>
    </div>
  </section>

  <!-- Right panel -->
  <section class="panel panel--right">
    <h2 class="headline headline--center abs" style="left:0; top:68px; width:400px;">Coaching &amp; Supervision<br>bedeutet für mich:</h2>
    <svg class="abs" style="left:0; top:150px;" width="400" height="150" viewBox="0 0 400 150" fill="none" stroke="#2a7f2a" stroke-width="1.6" stroke-linecap="round" stroke-linejoin="round">
      <line x1="93" y1="98" x2="120" y2="90"/>
      <line x1="187" y1="75" x2="213" y2="68"/>
      <line x1="280" y1="55" x2="307" y2="48"/>
      <circle cx="60" cy="104" r="33"/>
      <circle cx="153" cy="81" r="33"/>
      <circle cx="246" cy="60" r="33"/>
      <circle cx="340" cy="42" r="33"/>
      <!-- arm -->
      <path d="M50 92c4-4 10-4 12 0l-4 5c2 4 2 8 0 12 5-3 12-2 14 3 2 6-4 9-10 9H52c-4 0-6-4-5-9 1-6 1-13 3-20z"/>
      <!-- plant -->
      <path d="M153 95V80M153 84c-6-1-10-5-10-11 6 0 10 4 10 11zM153 82c1-7 5-11 12-11 0 7-5 11-12 11zM140 96h26M143 100h20"/>
      <!-- brush -->
      <path d="M262 42l-14 14M248 56c-4-1-8 2-8 6 0 3-1 5-4 6 5 2 10 1 12-3 2-3 2-6 0-9zM262 42c2-2 5 0 3 3"/>
      <!-- chart -->
      <path d="M324 56h32M328 56v-7h4v7M335 56v-10h4v10M342 56v-14h4v14M349 56v-18h4v18M326 44l10-8 6 4 12-10M350 30h4v4"/>
    </svg>
    <div class="step-label abs" style="left:10px; top:296px;">Ressourcen<br>stärken</div>
    <div class="step-label abs" style="left:103px; top:272px;">an den Heraus-<br>forderungen<br>wachsen</div>
    <div class="step-label abs" style="left:196px; top:252px;">das Leben<br>gestalten &amp;</div>
    <div class="step-label abs" style="left:290px; top:232px;">sich (weiter-)<br>entwickeln</div>

    <h2 class="headline headline--center abs" style="left:0; top:366px; width:400px;">Meine Grundhaltung:</h2>
    <ul class="values abs">
      <li>systemisch</li>
      <li>lösungs- und zielorientiert</li>
      <li>ressourcenorientiert</li>
      <li>wertschätzend</li>
    </ul>
    <p class="copy copy--justify abs" style="left:27px; top:510px; width:348px;">Ich habe keine „Beratungsschablonen“. Mir ist wichtig, mit welcher Arbeitsmethode Sie sich wohlfühlen. Deshalb passe ich die Methoden situativ Ihren Bedürfnissen an. Dazu bringe ich einen großen Methodenschatz mit. Be­sonders wichtig ist mir der Transfer in den Alltag.</p>
    <h2 class="headline headline--center abs" style="left:0; top:632px; width:400px;">Die Antwort auf Ihre Frage<br>liegt schon in Ihnen…</h2>
    <p class="copy abs" style="left:27px; top:710px; width:350px;">… ich helfe Ihnen, sie zu sehen. Und manchmal helfe ich auch, sich erstmal über die Frage klar zu werden.</p>
  </section>

</div>
</body>
</html>
```